Infographic for an online health and wellness tool. Breakdown of data in an easy to read format

The design we require is an infographic poster. We have an online tool that is used to audit companies on how healthy their employees are and how their employees feel regarding their employment. Simply put the online tool we have designed is used to health screen employees and ask specific questions regarding their current employment. The results are summarised and this data is used by the company to assist with workplace health and workforce planning. The data is collected and presented back to the company so they can target specific areas that are relevant to their company. This will enable the company to spend any available funds to areas that require improvement in the workforce. I have provided a sample infographic I have designed below, please don't laugh :) as an example of the data we collect. As this will only be a sample please feel free to change the data if you need or remove / simplify data if you think it would better. I would also like it if you highlighted three main areas that require action and some areas that do not require action and the company is doing well in. I have also attached an infographic design that I like

Corporate

Health And Wellness

Colors
33a6d7
85cae6
cee9f5
ec1f27
9bcb3c

Requirements
Must have
• Target areas that the company needs to address as a first priority. For example high number of lower back injuries, poor business culture, high obesity / sedentary rate
Nice to have
• Three categories that define the most important areas that require attention, second priority and things the company is doing extremely well in
• White background, clear and simple heading, modern icons, creativity
Should not have
• photos, not too many colours

```html
<!DOCTYPE html>
<html lang="en">
<head>
<meta charset="utf-8">
<title>Your Company Snapshot</title>
<link href="https://fonts.googleapis.com/css2?family=Fredoka:wght@500;600;700&family=Montserrat:wght@800&family=Roboto+Condensed:wght@400;500&display=swap" rel="stylesheet">
<style>
:root{
  --navy:#164a87;
  --blue:#1f5fa6;
  --sky:#33a6d7;
  --mist:#85cae6;
  --pale:#cee9f5;
  --band:#5fc9ef;
  --red:#ec1f27;
  --note:#f8ea5a;
  --ink:#1d2533;
  --white:#ffffff;
}
*{margin:0;padding:0;box-sizing:border-box}
html,body{width:891px;height:1200px;overflow:hidden;background:var(--white)}
.canvas{position:relative;width:891px;height:1200px;background:var(--white);font-family:"Roboto Condensed",sans-serif;color:var(--ink)}
.abs{position:absolute}

.brand{position:absolute;left:61px;top:50px;display:flex;align-items:center;gap:10px}
.brand-dot{width:26px;height:26px;border-radius:50%;background:var(--sky)}
.brand-name{font-family:"Fredoka",sans-serif;font-weight:600;font-size:25px;color:var(--navy);line-height:1}
.brand-line{position:absolute;left:97px;top:80px;font-family:"Roboto Condensed",sans-serif;font-size:10px;letter-spacing:1px;color:var(--sky)}

.title{position:absolute;left:0;top:118px;width:891px;text-align:center;font-family:"Montserrat",sans-serif;font-weight:800;font-size:50px;letter-spacing:-.5px;color:var(--navy);white-space:nowrap}

.section-head{position:absolute;height:40px;background:var(--navy);color:var(--white);font-family:"Fredoka",sans-serif;font-weight:600;font-size:15px;display:flex;align-items:center;justify-content:center;letter-spacing:.2px}
.panel{position:absolute;left:329px;top:250px;width:499px;height:678px;background:var(--pale)}
.info-band{position:absolute;left:329px;top:944px;width:495px;height:176px;background:var(--band)}

.sub-bar{position:absolute;height:20px;background:var(--navy);color:var(--white);font-family:"Fredoka",sans-serif;font-weight:600;font-size:12.5px;line-height:20px;padding-left:24px;white-space:nowrap}
.sub-bar.alert{background:var(--red)}
.sub-icon{position:absolute;width:42px;height:42px;border-radius:50%;background:var(--mist);display:flex;align-items:center;justify-content:center}
.sub-icon.alert{background:var(--red)}
.sub-icon svg{width:24px;height:24px}

.stat{position:absolute;width:110px;margin-left:-55px;text-align:center}
.stat .num{font-family:"Fredoka",sans-serif;font-weight:700;font-size:31px;line-height:34px;color:var(--blue)}
.stat .num.big{font-size:34px}
.stat .num.hot{color:var(--red)}
.stat .num.tight{font-size:28px}
.stat .lbl{font-size:10px;line-height:12.5px;color:var(--ink);margin-top:1px}
.stat .lbl.strong{font-family:"Fredoka",sans-serif;font-weight:600;font-size:20px;line-height:22px;color:var(--blue)}
.stat.narrow{width:64px;margin-left:-32px}

.note{position:absolute;background:var(--note);box-shadow:2px 3px 3px rgba(0,0,0,.18)}
.tape{position:absolute;width:22px;height:7px;background:#f07b7b;transform:rotate(-4deg)}

.figure{position:absolute;background:var(--mist);border-radius:22px 22px 8px 8px}
.avatars{position:absolute;height:74px;width:118px;border-radius:37px;background:var(--navy)}
</style>
</head>
<body>
<div class="canvas">

  <div class="brand"><span class="brand-dot"></span><span class="brand-name">HealthGauge</span></div>
  <div class="brand-line">WORKPLACE HEALTH INSIGHTS</div>

  <h1 class="title">YOUR COMPANY SNAPSHOT</h1>

  <!-- Left column -->
  <div class="section-head" style="left:54px;top:210px;width:243px">AGE COMPARISON</div>
  <div class="avatars" role="img" aria-label="Two employee avatars" style="left:52px;top:257px"></div>
  <div class="avatars" role="img" aria-label="Two employee avatars" style="left:181px;top:257px"></div>
  <div class="stat" style="left:110px;top:336px"><div class="lbl">Average age</div><div class="lbl strong">37 years</div></div>
  <div class="stat" style="left:240px;top:336px"><div class="lbl">Average health age</div><div class="lbl strong">45 years</div></div>

  <div class="section-head" style="left:54px;top:378px;width:243px">COMPANY ETHICS &amp; VALUES</div>
  <svg class="abs" style="left:86px;top:426px" width="48" height="42" viewBox="0 0 48 42" aria-hidden="true">
    <rect x="3" y="6" width="34" height="32" rx="3" fill="none" stroke="var(--mist)" stroke-width="4"/>
    <path d="M10 20 L19 30 L44 4" fill="none" stroke="var(--sky)" stroke-width="6" stroke-linecap="round" stroke-linejoin="round"/>
  </svg>
  <svg class="abs" style="left:215px;top:426px" width="48" height="42" viewBox="0 0 48 42" aria-hidden="true">
    <rect x="3" y="6" width="34" height="32" rx="3" fill="none" stroke="var(--mist)" stroke-width="4"/>
    <path d="M14 10 L42 38 M42 6 L14 34" fill="none" stroke="var(--sky)" stroke-width="6" stroke-linecap="round"/>
  </svg>
  <div class="stat" style="left:110px;top:468px"><div class="num big">44%</div><div class="lbl">Agree</div></div>
  <div class="stat" style="left:240px;top:468px"><div class="num big">31%</div><div class="lbl">Disagree</div></div>

  <div class="section-head" style="left:54px;top:520px;width:243px">INJURIES AND PAIN</div>
  <div class="figure" role="img" aria-label="Figure with right shoulder highlighted" style="left:90px;top:572px;width:40px;height:98px"></div>
  <div class="figure" role="img" aria-label="Figure holding lower back" style="left:218px;top:572px;width:46px;height:98px"></div>
  <div class="stat" style="left:110px;top:671px"><div class="num big">21%</div><div class="lbl">Right shoulder<br>injuries</div></div>
  <div class="stat" style="left:240px;top:671px"><div class="num big">19%</div><div class="lbl">Lumbar spine<br>injuries</div></div>

  <div class="section-head" style="left:54px;top:733px;width:243px">PHYSICAL HEALTH WEIGHT</div>
  <div class="figure" role="img" aria-label="Overweight body figure" style="left:86px;top:786px;width:50px;height:98px"></div>
  <div class="figure" role="img" aria-label="Average body figure" style="left:221px;top:786px;width:38px;height:98px"></div>
  <div class="stat" style="left:110px;top:883px"><div class="num big">69%</div><div class="lbl">Overweight or obese</div></div>
  <div class="stat" style="left:240px;top:883px"><div class="num big">63%</div><div class="lbl">National average</div></div>

  <div class="section-head" style="left:54px;top:938px;width:243px">SMOKING</div>
  <svg class="abs" style="left:82px;top:1010px" width="58" height="48" viewBox="0 0 58 48" aria-hidden="true">
    <path d="M38 4 C30 12 44 16 36 26" fill="none" stroke="var(--mist)" stroke-width="4" stroke-linecap="round"/>
    <rect x="2" y="34" width="40" height="11" fill="var(--mist)"/>
    <rect x="42" y="34" width="12" height="11" fill="var(--sky)"/>
  </svg>
  <svg class="abs" style="left:196px;top:990px" width="88" height="88" viewBox="0 0 88 88" aria-hidden="true">
    <rect x="18" y="42" width="44" height="10" fill="var(--sky)"/>
    <rect x="62" y="42" width="9" height="10" fill="var(--sky)"/>
    <circle cx="44" cy="44" r="38" fill="none" stroke="var(--sky)" stroke-width="9"/>
    <path d="M17 17 L71 71" stroke="var(--sky)" stroke-width="9"/>
  </svg>
  <div class="stat" style="left:110px;top:1081px"><div class="num big">71%</div><div class="lbl">Smokers</div></div>
  <div class="stat" style="left:240px;top:1081px"><div class="num big">29%</div><div class="lbl">Non smokers</div></div>

  <!-- Middle and right panel -->
  <div class="panel"></div>
  <div class="section-head" style="left:329px;top:210px;width:242px">WORKFORCE PLANNING</div>
  <div class="section-head" style="left:586px;top:210px;width:242px">CARDIOVASCULAR HEALTH</div>
  <div class="section-head" style="left:586px;top:589px;width:242px">PSYCHOLOGICAL HEALTH</div>

  <!-- Work life stage -->
  <div class="sub-bar" style="left:367px;top:267px;width:187px">Work life stage</div>
  <div class="sub-icon" style="left:346px;top:256px"><svg viewBox="0 0 24 24" aria-hidden="true"><rect x="3" y="8" width="18" height="12" rx="2" fill="var(--navy)"/><rect x="9" y="4" width="6" height="4" fill="none" stroke="var(--navy)" stroke-width="2"/></svg></div>
  <div class="stat" style="left:420px;top:297px"><div class="num">15%</div><div class="lbl">New entry</div></div>
  <div class="note" style="left:474px;top:294px;width:80px;height:68px"></div>
  <div class="tape" style="left:503px;top:290px"></div>
  <div class="stat" style="left:514px;top:297px"><div class="num hot">29%</div><div class="lbl">End career</div></div>

  <!-- Travel time -->
  <div class="sub-bar" style="left:367px;top:372px;width:187px">Travel time</div>
  <div class="sub-icon" style="left:346px;top:361px"><svg viewBox="0 0 24 24" aria-hidden="true"><path d="M2 13 L22 9 L22 12 L2 15 Z M9 12 L14 5 L16 5 L13 11 Z M9 14 L13 19 L15 19 L13 13 Z" fill="var(--navy)"/></svg></div>
  <div class="stat" style="left:420px;top:397px"><div class="num">32%</div><div class="lbl">Less than 1hr</div></div>
  <div class="stat" style="left:505px;top:397px"><div class="num">11%</div><div class="lbl">Greater than 4hrs</div></div>

  <!-- Career -->
  <div class="sub-bar" style="left:367px;top:471px;width:187px">Perceived career path</div>
  <div class="sub-icon" style="left:346px;top:460px"><svg viewBox="0 0 24 24" aria-hidden="true"><rect x="3" y="14" width="4" height="7" fill="var(--navy)"/><rect x="10" y="10" width="4" height="11" fill="var(--navy)"/><rect x="17" y="6" width="4" height="15" fill="var(--navy)"/><path d="M3 11 L10 6 L14 8 L21 2" fill="none" stroke="var(--navy)" stroke-width="2"/></svg></div>
  <div class="stat" style="left:420px;top:496px"><div class="num">41%</div><div class="lbl">Good<br>prospects</div></div>
  <div class="stat" style="left:508px;top:496px"><div class="num">8%</div><div class="lbl">Limited<br>opportunity</div></div>

  <!-- Engagement -->
  <div class="sub-bar" style="left:367px;top:586px;width:187px">Company engagement</div>
  <div class="sub-icon" style="left:346px;top:575px"><svg viewBox="0 0 24 24" aria-hidden="true"><circle cx="6" cy="9" r="3" fill="var(--navy)"/><circle cx="12" cy="7" r="3" fill="var(--navy)"/><circle cx="18" cy="9" r="3" fill="var(--navy)"/><rect x="3" y="13" width="18" height="7" rx="3" fill="var(--navy)"/></svg></div>
  <div class="stat" style="left:420px;top:613px"><div class="num">23%</div><div class="lbl">Little engagement</div></div>
  <div class="stat" style="left:506px;top:613px"><div class="num">8%</div><div class="lbl">Highly engaged</div></div>

  <!-- Physical health note -->
  <div class="note" style="left:342px;top:684px;width:222px;height:196px"></div>
  <svg class="abs" style="left:440px;top:660px" width="20" height="34" viewBox="0 0 20 34" aria-hidden="true"><circle cx="10" cy="9" r="7" fill="var(--red)"/><path d="M10 14 L10 32" stroke="#8a8a8a" stroke-width="2"/></svg>
  <div class="sub-bar alert" style="left:366px;top:718px;width:188px">Physical health</div>
  <div class="sub-icon alert" style="left:345px;top:707px"><svg viewBox="0 0 24 24" aria-hidden="true"><circle cx="14" cy="4" r="2.5" fill="var(--white)"/><path d="M6 9 L12 7 L15 12 L19 13 M12 7 L10 14 L14 17 L12 22 M10 14 L5 20" fill="none" stroke="var(--white)" stroke-width="2.4" stroke-linecap="round" stroke-linejoin="round"/></svg></div>
  <div class="stat narrow" style="left:410px;top:752px"><div class="num hot tight">49%</div><div class="lbl">Waist<br>circumference<br>high risk</div></div>
  <div class="stat narrow" style="left:474px;top:752px"><div class="num hot tight">18%</div><div class="lbl">Active for<br>more than<br>60min day</div></div>
  <div class="stat narrow" style="left:529px;top:752px"><div class="num hot tight">55%</div><div class="lbl">Sedentary<br>less than<br>30min day</div></div>

  <!-- Blood pressure -->
  <div class="sub-bar" style="left:624px;top:267px;width:172px">Blood pressure</div>
  <div class="sub-icon" style="left:603px;top:256px"><svg viewBox="0 0 24 24" aria-hidden="true"><rect x="3" y="4" width="8" height="10" rx="2" fill="none" stroke="var(--navy)" stroke-width="2"/><path d="M7 14 L7 20 L16 20 L16 10" fill="none" stroke="var(--navy)" stroke-width="2"/><rect x="14" y="4" width="6" height="7" rx="2" fill="var(--navy)"/></svg></div>
  <div class="stat" style="left:672px;top:297px"><div class="num">45%</div><div class="lbl">Normal blood<br>pressure</div></div>
  <div class="note" style="left:718px;top:294px;width:78px;height:68px"></div>
  <div class="tape" style="left:746px;top:290px"></div>
  <div class="stat" style="left:757px;top:297px"><div class="num hot">25%</div><div class="lbl">Elevated / high<br>blood pressure</div></div>

  <!-- Lipids -->
  <div class="sub-bar" style="left:624px;top:376px;width:172px">Blood lipids/cholesterol</div>
  <div class="sub-icon" style="left:603px;top:365px"><svg viewBox="0 0 24 24" aria-hidden="true"><circle cx="12" cy="12" r="10" fill="var(--navy)"/><circle cx="8" cy="13" r="2" fill="var(--mist)"/><circle cx="13" cy="9" r="2" fill="var(--mist)"/><circle cx="15" cy="15" r="2" fill="var(--mist)"/></svg></div>
  <div class="stat" style="left:672px;top:405px"><div class="num">58%</div><div class="lbl">Normal range<br>levels</div></div>
  <div class="stat" style="left:752px;top:405px"><div class="num">15%</div><div class="lbl">Elevated / high<br>lipid levels</div></div>

  <!-- Glucose -->
  <div class="sub-bar" style="left:624px;top:488px;width:172px">Blood glucose</div>
  <div class="sub-icon" style="left:603px;top:477px"><svg viewBox="0 0 24 24" aria-hidden="true"><path d="M12 2 C8 9 5 12 5 15 A7 7 0 0 0 19 15 C19 12 16 9 12 2 Z" fill="var(--navy)"/></svg></div>
  <div class="stat" style="left:672px;top:521px"><div class="num">38%</div><div class="lbl">Normal<br>levels</div></div>
  <div class="stat" style="left:755px;top:521px"><div class="num">17%</div><div class="lbl">Elevated / high<br>glucose levels</div></div>

  <!-- Depression: rain cloud -->
  <div class="sub-bar" style="left:624px;top:646px;width:172px">Depression</div>
  <div class="sub-icon" style="left:603px;top:635px"><svg viewBox="0 0 24 24" aria-hidden="true"><path d="M6 14 A4 4 0 0 1 7 6 A5 5 0 0 1 16 5 A4 4 0 0 1 18 14 Z" fill="var(--navy)"/><path d="M8 17 L7 21 M12 17 L11 21 M16 17 L15 21" stroke="var(--navy)" stroke-width="2" stroke-linecap="round"/></svg></div>
  <div class="stat" style="left:672px;top:671px"><div class="num">60%</div><div class="lbl">No concerns<br>with depressions</div></div>
  <div class="stat" style="left:754px;top:671px"><div class="num">10%</div><div class="lbl">Report severe cases<br>of depression</div></div>

  <!-- Stress: lightning bolt -->
  <div class="sub-bar" style="left:624px;top:741px;width:172px">Stress</div>
  <div class="sub-icon" style="left:603px;top:730px"><svg viewBox="0 0 24 24" aria-hidden="true"><path d="M14 2 L5 14 L11 14 L9 22 L19 9 L13 9 Z" fill="var(--navy)"/></svg></div>
  <div class="stat" style="left:672px;top:767px"><div class="num">24%</div><div class="lbl">Moderate levels<br>of stress</div></div>
  <div class="stat" style="left:754px;top:767px"><div class="num">8%</div><div class="lbl">Severe cases<br>of stress</div></div>

  <!-- Anxiety: jagged pulse -->
  <div class="sub-bar" style="left:624px;top:847px;width:172px">Anxiety</div>
  <div class="sub-icon" style="left:603px;top:836px"><svg viewBox="0 0 24 24" aria-hidden="true"><path d="M2 12 L6 12 L8 6 L11 18 L14 4 L17 16 L19 12 L22 12" fill="none" stroke="var(--navy)" stroke-width="2.4" stroke-linecap="round" stroke-linejoin="round"/></svg></div>
  <div class="stat" style="left:672px;top:871px"><div class="num">72%</div><div class="lbl">Not at all</div></div>
  <div class="stat" style="left:754px;top:871px"><div class="num">4%</div><div class="lbl">severe</div></div>

  <!-- General information -->
  <div class="info-band"></div>
  <div class="section-head" style="left:329px;top:944px;width:242px">GENERAL INFORMATION</div>

  <svg class="abs" style="left:352px;top:996px" width="60" height="52" viewBox="0 0 60 52" aria-hidden="true">
    <path d="M30 50 L6 26 A14 14 0 0 1 30 8 A14 14 0 0 1 54 26 Z" fill="var(--white)"/>
    <path d="M6 26 L20 26 L25 18 L31 34 L36 24 L54 24" fill="none" stroke="var(--band)" stroke-width="3"/>
  </svg>
  <svg class="abs" style="left:460px;top:994px" width="34" height="56" viewBox="0 0 34 56" aria-hidden="true">
    <rect x="3" y="2" width="28" height="36" rx="6" fill="var(--white)"/>
    <path d="M17 10 C14 16 12 18 12 21 A5 5 0 0 0 22 21 C22 18 20 16 17 10 Z" fill="var(--band)"/>
    <rect x="12" y="38" width="10" height="10" fill="var(--white)"/>
    <rect x="15" y="48" width="4" height="6" fill="var(--white)"/>
  </svg>
  <svg class="abs" style="left:553px;top:994px" width="40" height="56" viewBox="0 0 40 56" aria-hidden="true">
    <circle cx="20" cy="18" r="14" fill="none" stroke="var(--white)" stroke-width="5"/>
    <path d="M20 32 L20 54 M12 44 L28 44" stroke="var(--white)" stroke-width="5"/>
  </svg>
  <svg class="abs" style="left:634px;top:1000px" width="64" height="46" viewBox="0 0 64 46" aria-hidden="true">
    <rect x="3" y="3" width="46" height="32" fill="none" stroke="var(--white)" stroke-width="4"/>
    <path d="M3 3 L26 22 L49 3" fill="none" stroke="var(--white)" stroke-width="4"/>
    <path d="M62 40 C58 28 50 24 40 24 L40 18 L30 28 L40 38 L40 32 C48 32 56 34 62 40 Z" fill="var(--navy)"/>
  </svg>
  <div class="stat" style="left:382px;top:1053px"><div class="num">6%</div><div class="lbl">Cardiovascular<br>disease</div></div>
  <div class="stat" style="left:477px;top:1053px"><div class="num">14%</div><div class="lbl">Type<br>2 diabetes</div></div>
  <div class="stat" style="left:573px;top:1053px"><div class="num">55%</div><div class="lbl">Female</div></div>
  <div class="stat" style="left:668px;top:1053px"><div class="num">75%</div><div class="lbl">Responded</div></div>

  <div class="note" style="left:712px;top:988px;width:114px;height:130px"></div>
  <svg class="abs" style="left:760px;top:975px" width="16" height="26" viewBox="0 0 16 26" aria-hidden="true"><circle cx="8" cy="7" r="5.5" fill="var(--red)"/><path d="M8 11 L8 25" stroke="#8a8a8a" stroke-width="2"/></svg>
  <svg class="abs" style="left:745px;top:1002px" width="46" height="46" viewBox="0 0 46 46" aria-hidden="true">
    <path d="M23 3 A20 20 0 1 1 9 37 L4 44 L6 33 A20 20 0 0 1 23 3 Z" fill="var(--red)"/>
    <path d="M14 16 L22 16 L14 26 L22 26 M25 14 L32 14 L25 22 L32 22" fill="none" stroke="var(--note)" stroke-width="2.6" stroke-linejoin="round"/>
  </svg>
  <div class="stat" style="left:768px;top:1053px"><div class="num hot big">25%</div><div class="lbl">Work-related<br>sleep difficulties</div></div>

</div>
</body>
</html>
```